Shopify Design for a Homeopathic Shop

The design should let the user give a feeling of luxury and naturality(earthy).

We want to build up a alternative medicine luxury brand. The user should have a feeling of trust when visiting our shop. We stand for natural remedies.

Target Market(s)

Alternative / Left

Industry/Entity Type

Alternative Medicine

Font styles to use
Sans Serif

Colors

Designer to choose colors to be used in the design.

```html
<!DOCTYPE html>
<html lang="en">
<head>
<meta charset="utf-8">
<title>VerdaRoot — Homeopathic Remedies</title>
<link href="https://fonts.googleapis.com/css2?family=Lato:wght@300;400;700;900&display=swap" rel="stylesheet">
<style>
:root{
  --green:#7cbb2e;
  --green-dark:#1f7a3b;
  --ink:#2b2b2b;
  --text:#444;
  --muted:#666;
  --price:#b5342a;
  --dark:#232323;
  --darker:#1a1a1a;
  --light:#f5f5f5;
  --white:#fff;
}
*{box-sizing:border-box;margin:0;padding:0}
html,body{width:1200px;height:3738px;overflow:hidden}
body{font-family:'Lato',sans-serif;color:var(--text);background:var(--white);position:relative}
.abs{position:absolute}
a{color:inherit;text-decoration:none}

/* top bar */
.topbar{left:0;top:0;width:1200px;height:32px;background:var(--ink);color:#ddd;font-size:13px}
.topbar .lang{left:80px;top:8px;display:flex;gap:6px;align-items:center}
.topbar .flag{width:18px;height:12px;background:linear-gradient(#b22 50%,#eee 50%);display:inline-block}
.topbar .cur{left:202px;top:8px}
.topbar .sep{left:180px;top:6px;width:1px;height:20px;background:#555}
.topbar .social{left:518px;top:0;display:flex}
.topbar .social span{width:34px;height:32px;display:flex;align-items:center;justify-content:center}
.topbar .social span:first-child{background:var(--green)}
.topbar .social i{display:block;width:9px;height:9px;border-radius:2px;background:#eee}
.topbar .acct{right:80px;top:8px}

/* nav */
.nav{left:0;top:32px;width:1200px;height:91px;border-bottom:1px solid #eee}
.logo{display:flex;flex-direction:column;line-height:1}
.logo b{font-weight:400;font-size:28px;letter-spacing:1px;color:var(--green-dark)}
.logo small{font-size:6px;letter-spacing:4px;color:var(--muted);margin-top:3px}
.nav .logo{left:77px;top:30px}
.nav ul{left:465px;top:38px;display:flex;gap:46px;list-style:none;font-size:14px;color:#555}
.nav ul li.on{color:var(--green);font-weight:700}
.nav .icons{right:80px;top:34px;display:flex;gap:22px}

/* hero */
.hero{left:0;top:123px;width:1200px;height:504px;background:linear-gradient(120deg,#6f7377 0%,#a9adb0 45%,#d7d4cc 70%,#8e8a84 100%)}
.hero h1{left:83px;top:200px;font-size:34px;font-weight:900;color:var(--white)}
.hero p{left:80px;top:250px;width:350px;font-size:13px;color:var(--white);line-height:1.3}
.btn{background:var(--green);color:var(--white);font-size:14px;display:flex;align-items:center;justify-content:center}
.hero .btn{left:80px;top:306px;width:152px;height:36px}
.hero .arrow{top:240px}
.dots{display:flex;gap:10px}
.dots i{width:9px;height:9px;border-radius:50%;background:var(--white)}
.dots i.on{background:var(--green)}
.hero .dots{left:567px;top:467px}

/* promo tiles */
.tile{top:692px;height:251px;color:var(--white)}
.tile h3{position:absolute;font-size:18px;font-weight:700;line-height:1.25;letter-spacing:.5px}
.tile-a{left:81px;width:238px;background:linear-gradient(160deg,#5b4a35,#8a7a5c 55%,#3d3020)}
.tile-b{left:345px;width:511px;background:linear-gradient(120deg,#2e3d28,#4a5d3a 50%,#2b3426)}
.tile-c{left:882px;width:238px;background:linear-gradient(160deg,#b84a2c,#7a6a50 50%,#5a4630)}
.tile-b .offer{left:170px;top:60px;font-size:25px;font-weight:300;line-height:1.15}
.tile-b .offer b{font-weight:700}
.tile-b .badge{left:228px;top:63px;width:54px;height:54px;border-radius:50%;background:var(--green);font-size:18px;font-weight:700;display:flex;align-items:center;justify-content:center}

/* featured */
.section-title{font-size:37px;font-weight:400;color:var(--ink);text-align:center}
.featured-title{left:0;top:990px;width:1200px}
.product{top:1072px;width:238px;text-align:center}
.product .shot{height:251px;background:linear-gradient(#f4f4f4,#ebebeb)}
.product .name{margin-top:18px;font-size:14px;letter-spacing:1.5px;color:#333}
.product .price{margin-top:8px;font-size:14px;letter-spacing:1px;color:var(--price)}
.product .btn{margin:14px auto 0;width:142px;height:35px;font-size:14px;letter-spacing:1px}
.slide-arrow{width:24px;height:30px}

/* feature band */
.band{left:0;top:1538px;width:1200px;height:462px;background:linear-gradient(90deg,#ecece9,#f4f4f2 50%,#e9e9e6)}
.band .leaf-l{left:0;top:300px;width:110px;height:162px;background:linear-gradient(45deg,#9cc27c,rgba(156,194,124,0))}
.band h2{left:142px;top:120px;font-size:32px;font-weight:400;color:var(--ink)}
.band .q{left:142px;top:172px;font-size:14px;letter-spacing:1px;color:#333}
.band p{left:142px;top:206px;width:430px;font-size:14px;letter-spacing:1px;line-height:1.3;color:#333}
.band .price{left:143px;top:274px;font-size:20px;letter-spacing:1.5px;color:var(--price)}
.band .btn{left:143px;top:313px;width:142px;height:36px;letter-spacing:1px}
.band .bottles{left:600px;top:40px;width:440px;height:420px;background:radial-gradient(ellipse at center,#cfd6cf 0%,#e8e8e4 60%,rgba(240,240,238,0) 75%)}

/* blogs */
.blogs-title{left:81px;top:2100px;width:438px}
.post{left:81px;width:520px;height:157px}
.post .img{left:0;top:0;width:200px;height:157px}
.post h4{left:225px;top:8px;font-size:19px;font-weight:400;color:#222}
.post .date{left:225px;top:40px;font-size:14px;color:#444}
.post p{left:225px;top:66px;width:270px;font-size:13px;line-height:1.35;color:#555}
.post .more{left:226px;top:134px;font-size:13px;color:#444;text-decoration:underline}
.blog-nav{left:272px;top:2566px;display:flex;gap:8px}
.blog-nav span{width:29px;height:29px;border:1.5px solid #333;border-radius:50%;display:flex;align-items:center;justify-content:center}
.blog-nav span.on{border-color:var(--green-dark)}

/* testimonials */
.testi-title{left:601px;top:2102px;width:519px}
.testi{left:601px;top:2171px;width:519px;height:438px;background:#f4f4f4;text-align:center}
.testi .avatar{left:194px;top:30px;width:134px;height:134px;border-radius:50%;border:4px solid var(--white);background:radial-gradient(circle at 50% 40%,#e4d6c7,#b9a595)}
.testi .who{left:0;top:196px;width:519px;font-size:18px;font-weight:700;color:#222}
.testi .role{left:0;top:221px;width:519px;font-size:14px;color:var(--green-dark)}
.testi p{left:100px;top:249px;width:320px;font-size:13px;line-height:1.3;color:#444}
.testi .mark{font-size:28px;font-weight:900;color:#333}
.testi .stars{left:0;top:301px;width:519px;font-size:16px;color:#f0a01e;letter-spacing:1px}
.testi .dots{left:240px;top:363px;gap:5px}
.testi .dots i{width:7px;height:7px;background:#bbb}
.testi .dots i.on{background:var(--green)}

/* about */
.about-img{left:81px;top:2710px;width:520px;height:344px;background:linear-gradient(160deg,#6aa53a,#9fc45d 45%,#7a5a3c 85%)}
.play{left:214px;top:124px;width:54px;height:54px;border-radius:50%;border:3px solid rgba(255,255,255,.85);display:flex;align-items:center;justify-content:center}
.about h2{left:633px;top:2740px;font-size:37px;font-weight:400;color:var(--ink)}
.about p{left:637px;width:470px;font-size:13px;line-height:1.3;color:#444}
.about .btn{left:637px;top:2979px;width:173px;height:45px}

/* help & newsletter */
.help{left:0;top:3125px;width:599px;height:307px;background:var(--green-dark);color:var(--white)}
.news{left:599px;top:3125px;width:601px;height:307px;background:var(--green);color:var(--white)}
.help h2,.news h2{position:absolute;font-size:32px;font-weight:400}
.help h2{left:79px;top:63px}
.help .row{position:absolute;left:80px;display:flex;gap:14px;font-size:14px;align-items:center}
.help .rule{left:80px;top:140px;width:358px;height:1px;background:var(--white)}
.news h2{left:65px;top:63px}
.news p{left:64px;top:120px;width:470px;font-size:14px;line-height:1.65}
.news .field{left:55px;top:179px;width:466px;height:58px;border-radius:29px;background:var(--white);color:#555;font-size:14px;padding-left:30px;display:flex;align-items:center}
.news .send{right:15px;top:12px;width:34px;height:34px;border-radius:50%;background:var(--green);display:flex;align-items:center;justify-content:center}

/* footer */
.footer{left:0;top:3432px;width:1200px;height:254px;background:var(--dark);color:#ddd}
.footer .logo{left:80px;top:52px}
.footer .logo b{color:var(--white)}
.footer .logo small{color:#bbb}
.footer h5{position:absolute;top:54px;font-size:18px;font-weight:400;letter-spacing:.5px;color:var(--white)}
.footer ul{position:absolute;list-style:none;font-size:13.5px}
.footer ul li{height:25.5px}
.footer ul li::before{content:'>';margin-right:14px;font-size:11px}
.footer ul.social li::before{content:none}
.footer ul.social li{display:flex;align-items:center;gap:14px}
.footer ul.social i{width:17px;height:17px;border-radius:50%;display:inline-block}
.copy{left:0;top:3686px;width:1200px;height:52px;background:var(--darker);border-top:1px solid #444;color:#ddd;font-size:13.5px}
.copy span{position:absolute;left:80px;top:16px;letter-spacing:.5px}
.pay{right:80px;top:12px;display:flex;gap:7px}
.pay i{width:42px;height:27px;background:#e8e8e8;border-radius:2px;display:block}
</style>
</head>
<body>

<header class="abs topbar">
  <div class="abs lang"><span class="flag"></span> English ▾</div>
  <div class="abs sep"></div>
  <div class="abs cur">$ USD ▾</div>
  <div class="abs social"><span><i></i></span><span><i></i></span><span><i></i></span><span><i></i></span><span><i></i></span></div>
  <div class="abs acct">Register Or Sign In</div>
</header>

<nav class="abs nav">
  <div class="abs logo"><b>VERDAROOT</b><small>HOMEOPATHIC REMEDIES</small></div>
  <ul class="abs">
    <li class="on">Home</li><li>About us</li><li>Shop</li><li>Offer</li><li>Blogs</li><li>Contact us</li>
  </ul>
  <div class="abs icons">
    <svg width="22" height="22" viewBox="0 0 22 22" fill="none" stroke="#222" stroke-width="2"><circle cx="9" cy="9" r="7"/><path d="M14 14l6 6"/></svg>
    <svg width="22" height="22" viewBox="0 0 24 24" fill="none" stroke="#222" stroke-width="2"><path d="M12 21l-8-8a5 5 0 017-7l1 1 1-1a5 5 0 017 7z"/></svg>
    <svg width="22" height="22" viewBox="0 0 24 24" fill="none" stroke="#222" stroke-width="2"><path d="M2 3h3l3 12h11l2-8H7"/><circle cx="9" cy="20" r="1.5"/><circle cx="18" cy="20" r="1.5"/></svg>
  </div>
</nav>

<section class="abs hero" role="img" aria-label="Shopping cart filled with homeopathic remedy bottles in front of a laptop">
  <h1 class="abs">The Right Remedy For You</h1>
  <p class="abs">Lorem Ipsum is simply dummy text of the printing and typesetting industry.</p>
  <a class="abs btn">Shop Now &gt;&gt;</a>
  <svg class="abs arrow" style="left:30px" width="24" height="30" viewBox="0 0 24 30"><path d="M18 3L6 15l12 12" fill="none" stroke="#fff" stroke-width="4" opacity=".8"/></svg>
  <svg class="abs arrow" style="right:30px" width="24" height="30" viewBox="0 0 24 30"><path d="M6 3l12 12L6 27" fill="none" stroke="#fff" stroke-width="4" opacity=".8"/></svg>
  <div class="abs dots"><i class="on"></i><i></i><i></i><i></i></div>
</section>

<div class="abs tile tile-a" role="img" aria-label="Remedy globules and small glass vials with dried flowers"><h3 style="left:18px;top:178px">Complete<br>Range of Medication</h3></div>
<div class="abs tile tile-b" role="img" aria-label="Remedy bottles and globules among green plants and flowers">
  <div class="abs offer">Upto<br>Off<br><b>Homeopathic</b><br>Products</div>
  <div class="abs badge">50%</div>
</div>
<div class="abs tile tile-c" role="img" aria-label="Amber dropper bottle among red poppy flowers"><h3 style="left:24px;top:183px">Complete<br>Range of Medication</h3></div>

<h2 class="abs section-title featured-title">Featured Products</h2>
<svg class="abs slide-arrow" style="left:28px;top:1189px" viewBox="0 0 24 30"><path d="M18 3L6 15l12 12" fill="none" stroke="#888" stroke-width="4"/></svg>
<svg class="abs slide-arrow" style="right:28px;top:1189px" viewBox="0 0 24 30"><path d="M6 3l12 12L6 27" fill="none" stroke="#888" stroke-width="4"/></svg>
<div class="abs product" style="left:80px"><div class="shot" role="img" aria-label="Amber dilution bottle with red dropper cap"></div><div class="name">Product Name</div><div class="price">$00.00</div><div class="btn">Add To Cart</div></div>
<div class="abs product" style="left:347px"><div class="shot" role="img" aria-label="Tablet jar beside its pink product box"></div><div class="name">Product Name</div><div class="price">$00.00</div><div class="btn">Add To Cart</div></div>
<div class="abs product" style="left:615px"><div class="shot" role="img" aria-label="Mother tincture bottle with blue cap beside its box"></div><div class="name">Product Name</div><div class="price">$00.00</div><div class="btn">Add To Cart</div></div>
<div class="abs product" style="left:884px"><div class="shot" role="img" aria-label="Drops bottle beside its yellow product box"></div><div class="name">Product Name</div><div class="price">$00.00</div><div class="btn">Add To Cart</div></div>

<section class="abs band">
  <div class="abs leaf-l" role="img" aria-label="Soft green leaves"></div>
  <h2 class="abs">Food Allergies</h2>
  <div class="abs q">What is Lorem Ipsum?</div>
  <p class="abs">Lorem Ipsum is simply dummy text of the printing and typesetting industry. Lorem Ipsum has been the industry standard dummy text ever since the 1500s,</p>
  <div class="abs price">$00.00</div>
  <div class="abs btn">Add To Cart</div>
  <div class="abs bottles" role="img" aria-label="Row of amber spray bottles around a white probiotic jar"></div>
</section>

<h2 class="abs section-title blogs-title">Blogs</h2>
<article class="abs post" style="top:2174px">
  <div class="abs img" role="img" aria-label="Essential oil bottles with flowers on a wooden slice" style="background:linear-gradient(135deg,#e9e3d8,#a98a5e 60%,#6c4d2c)"></div>
  <h4 class="abs">Blog Title Heading 01</h4><div class="abs date">June 25, 2019</div>
  <p class="abs">Lorem Ipsum is simply dummy text of the printing typesetting industry&nbsp; Ipsum has industryin the standard dummy.</p>
  <a class="abs more">Read More</a>
</article>
<article class="abs post" style="top:2368px">
  <div class="abs img" role="img" aria-label="Mother giving remedy drops to a child" style="background:linear-gradient(135deg,#f0ece6,#d9c2a6 55%,#b98f6b)"></div>
  <h4 class="abs">Blog Title Heading 01</h4><div class="abs date">June 25, 2019</div>
  <p class="abs">Lorem Ipsum is simply dummy text of the printing typesetting industry&nbsp; Ipsum has industryin the standard dummy.</p>
  <a class="abs more">Read More</a>
</article>
<div class="abs blog-nav">
  <span><svg width="10" height="12" viewBox="0 0 10 12"><path d="M7 1L2 6l5 5" fill="none" stroke="#333" stroke-width="1.8"/></svg></span>
  <span class="on"><svg width="10" height="12" viewBox="0 0 10 12"><path d="M3 1l5 5-5 5" fill="none" stroke="#1f7a3b" stroke-width="1.8"/></svg></span>
</div>

<h2 class="abs section-title testi-title">Testimonials</h2>
<section class="abs testi">
  <div class="abs avatar" role="img" aria-label="Customer portrait"></div>
  <div class="abs who">Clara Whitmore</div>
  <div class="abs role">Director</div>
  <p class="abs"><span class="abs mark" style="left:-20px;top:-14px">“</span>Lorem Ipsum is simply dummy text of the printing typesetting industry&nbsp; Ipsum has been theindustry in the standard dummy<span class="abs mark" style="right:-22px;top:22px">”</span></p>
  <div class="abs stars">★★★★★</div>
  <div class="abs dots"><i class="on"></i><i></i><i></i></div>
</section>

<section class="about">
  <div class="abs about-img" role="img" aria-label="Mortar with daisies and lavender on an old book in a meadow">
    <div class="abs play"><svg width="18" height="20" viewBox="0 0 18 20"><path d="M3 2l13 8-13 8z" fill="none" stroke="#fff" stroke-width="2.5"/></svg></div>
  </div>
  <h2 class="abs">About us</h2>
  <p class="abs" style="top:2822px">Lorem Ipsum is simply dummy text of the printing and typesetting&nbsp; Lorem Ipsum has been the industry's standard dummy a type specimen booking text ever since the 1500s,</p>
  <p class="abs" style="top:2887px">when an unknown printer took a galley of type and scrambled it to make a type specimen book. It has survived not only five centuries, but also the leap into electronic typesetting, remaining essentially unchanged. It was un popularised in the 1960s</p>
  <a class="abs btn">Read More</a>
</section>

<section class="abs help">
  <h2>Need Help?</h2>
  <div class="row" style="top:111px"><svg width="18" height="13" viewBox="0 0 18 13"><rect x="1" y="1" width="16" height="11" fill="#fff"/><path d="M1 1l8 6 8-6" fill="none" stroke="#1f7a3b" stroke-width="1.5"/></svg><span>:</span><span>info@verdaroot.com</span></div>
  <div class="abs rule"></div>
  <div class="row" style="top:173px"><svg width="16" height="16" viewBox="0 0 16 16"><path d="M3 1l3 3-2 2c1 2 3 4 5 5l2-2 3 3-2 3C7 15 1 9 1 3z" fill="#fff"/></svg><span>:</span><span>+00 123 456 7890</span></div>
  <div class="row" style="top:197px"><svg width="16" height="16" viewBox="0 0 16 16"><circle cx="8" cy="8" r="7" fill="#fff"/><path d="M8 4v4h3" stroke="#1f7a3b" stroke-width="1.6" fill="none"/></svg><span>:</span><span>Monday - Saturday 9:00 -18:00hrs.</span></div>
</section>

<section class="abs news">
  <h2>Newsletter Signup</h2>
  <p class="abs">Please subscribe and receive our latest news, promotions, events, and clinic updates you can't get anywhere else.</p>
  <div class="abs field">Enter your email here*
    <span class="abs send"><svg width="16" height="16" viewBox="0 0 16 16"><path d="M1 8l14-7-4 14-3-6z" fill="#fff"/></svg></span>
  </div>
</section>

<footer class="abs footer">
  <div class="abs logo"><b>VERDAROOT</b><small>HOMEOPATHIC REMEDIES</small></div>
  <ul style="left:80px;top:96px"><li>Home</li><li>About us</li><li>Shop</li><li>Blogs</li><li>Contact us</li></ul>
  <h5 style="left:384px">Why Buy From us</h5>
  <ul style="left:384px;top:96px"><li>Shipping &amp; Returns</li><li>Secure Shopping</li><li>International Shopping</li><li>Group Sales</li><li>Affiliates</li></ul>
  <h5 style="left:702px">My Account</h5>
  <ul style="left:702px;top:96px"><li>Sign In</li><li>View Cart</li><li>My Product</li><li>Track My Order</li><li>Help</li></ul>
  <h5 style="left:1026px">Follow us</h5>
  <ul class="social" style="left:1026px;top:98px">
    <li><i style="background:#3b5998"></i>Gathernet</li>
    <li><i style="background:#d6336c"></i>Picstream</li>
    <li><i style="background:#1da1f2"></i>Chirper</li>
    <li><i style="background:#0a77b5"></i>Worklink</li>
    <li><i style="background:#e02020"></i>Viewtube</li>
  </ul>
</footer>

<div class="abs copy">
  <span>Copyright©2019 Verdaroot, All right reserved</span>
  <div class="abs pay"><i></i><i></i><i></i><i></i><i></i></div>
</div>

</body>
</html>
```